Delvane Pitching Mechanics

Private pitching sessions with a Division 1 WJAL baseball pitcher. Would also like a page setup where clients can request sesseions and pay for sessions.

```html
<!DOCTYPE html>
<html lang="en">
<head>
<meta charset="utf-8">
<title>Delvane Pitching Mechanics</title>
<link href="https://fonts.googleapis.com/css2?family=Audiowide&family=Lato:wght@400;700&display=swap" rel="stylesheet">
<style>
:root{
  --red:#ee2a3f;
  --red-dark:#d81f35;
  --ink:#111111;
  --text:#333333;
  --pink:#fde8ea;
  --white:#ffffff;
  --black:#000000;
}
*{box-sizing:border-box;margin:0;padding:0}
html,body{width:1200px;height:3438px;overflow:hidden;background:var(--white)}
body{position:relative;font-family:'Lato',sans-serif;color:var(--text)}
.display{font-family:'Audiowide',sans-serif;font-weight:400}
.abs{position:absolute}
.photo{position:absolute}
.btn{position:absolute;background:var(--red);color:var(--white);font-family:'Audiowide',sans-serif;display:flex;align-items:center;justify-content:center;border-radius:3px;box-shadow:0 3px 8px rgba(0,0,0,.2)}

/* header */
.brand{left:113px;top:16px;font-family:'Audiowide',sans-serif;color:var(--red);font-size:46px;line-height:1}
.brand-sub{left:113px;top:64px;font-family:'Audiowide',sans-serif;color:var(--red);font-size:8px;letter-spacing:.3px}
.nav a{position:absolute;top:32px;font-family:'Audiowide',sans-serif;font-size:15px;color:var(--ink);text-decoration:none}
.nav a.active{color:var(--red);text-decoration:underline}
.nav-cta{left:948px;top:17px;width:141px;height:51px;font-size:18px}

/* hero */
.hero{left:0;top:87px;width:1200px;height:551px;border-radius:44px;overflow:hidden;background:linear-gradient(100deg,#1d2a2c 0%,#4a5a4f 45%,#6b6b5a 70%,#3c3a36 100%)}
.hero::after{content:"";position:absolute;inset:0;background:linear-gradient(90deg,rgba(0,0,0,.55),rgba(0,0,0,.1))}
.hero-welcome{left:113px;top:222px;color:var(--white);font-size:22px;z-index:2}
.hero-title{left:108px;top:260px;color:var(--white);font-size:48px;line-height:56px;z-index:2}
.hero-text{left:111px;top:378px;width:520px;color:var(--white);font-size:15px;line-height:31px;z-index:2}
.hero-btn{left:111px;top:450px;width:140px;height:48px;font-size:17px;z-index:2}
.contact-card{left:667px;top:227px;width:424px;height:271px;border-radius:34px;background:rgba(255,255,255,.72);z-index:2}
.contact-card h2{position:absolute;left:35px;top:36px;font-family:'Audiowide',sans-serif;font-size:22px;color:var(--ink);font-weight:400}
.contact-card p{position:absolute;left:35px;top:73px;font-size:15px;color:#555}
.contact-card .field{position:absolute;left:35px;top:105px;width:355px;height:52px;border:1.5px solid #333;background:rgba(255,255,255,.3)}
.contact-card .btn{left:35px;top:176px;width:221px;height:50px;font-size:17px}
.dots{left:574px;top:558px;z-index:2;display:flex;gap:10px}
.dots span{width:11px;height:11px;border-radius:50%;background:rgba(255,255,255,.55)}
.dots span.on{background:var(--red)}

/* about */
.eyebrow{font-family:'Audiowide',sans-serif;font-size:22px;color:var(--ink)}
.eyebrow em,.section-title em{font-style:normal;color:var(--red)}
.about-eyebrow{left:111px;top:712px}
.about-title{left:109px;top:752px;font-size:34px;line-height:42px;color:var(--ink)}
.about-lead{left:111px;top:840px;width:405px;font-size:18px;line-height:34px;color:var(--ink)}
.about-body{left:579px;top:708px;width:505px;font-size:15px;line-height:31px;color:var(--text)}
.about-frame{left:509px;top:1028px;width:420px;height:356px;border:6px solid var(--red);border-radius:8px}
.photo-pitch{left:586px;top:1000px;width:502px;height:344px;background:linear-gradient(135deg,#8c8f6c,#b7ad86 45%,#6f6a52)}
.photo-dive{left:111px;top:1065px;width:581px;height:346px;background:linear-gradient(135deg,#1f3346,#3f5a6f 40%,#7a5a3c 75%,#5a3d25)}

/* services */
.services{left:0;top:1499px;width:1200px;height:564px;background:var(--pink)}
.section-title{position:absolute;left:0;width:1200px;text-align:center;font-family:'Audiowide',sans-serif;font-weight:400;font-size:34px;color:var(--ink)}
.card{position:absolute;top:1622px;width:316px;height:363px;background:var(--white);border-radius:10px;border-bottom:5px solid var(--ink)}
.card.featured{border-bottom-color:var(--red-dark)}
.card .photo{left:10px;top:8px;width:296px;height:246px;border-radius:8px}
.card h3{position:absolute;left:0;width:100%;top:276px;text-align:center;font-family:'Audiowide',sans-serif;font-weight:400;font-size:20px;color:var(--ink)}
.card a{position:absolute;left:0;width:100%;top:309px;text-align:center;font-family:'Audiowide',sans-serif;font-size:17px;color:var(--red);text-decoration:none}
.circle-arrow{position:absolute;width:28px;height:28px}

/* division band */
.band{left:0;top:2063px;width:1200px;height:395px;background:linear-gradient(180deg,#e52b45,#e3334a 60%,#dc2c42)}
.band-title{position:absolute;left:0;width:1200px;top:2118px;text-align:center;font-family:'Audiowide',sans-serif;font-weight:400;font-size:34px;color:var(--white)}
.band-text{left:125px;top:2172px;width:950px;text-align:center;color:var(--white);font-size:15px;line-height:31px}
.band-btn{left:527px;top:2347px;width:147px;height:47px;background:var(--white);color:var(--red);font-family:'Audiowide',sans-serif;font-size:17px;display:flex;align-items:center;justify-content:center}

/* gallery */
.gallery .photo{top:2590px;width:235px;height:324px}
.chev{position:absolute;top:2744px;width:14px;height:18px}

/* footer */
.footer{left:0;top:2994px;width:1200px;height:444px;background:var(--black)}
.footer-heading{position:absolute;top:3053px;font-family:'Audiowide',sans-serif;font-weight:400;font-size:22px;line-height:28px;color:var(--white)}
.quick{left:113px;top:3096px;list-style:none}
.quick li{display:flex;align-items:center;gap:14px;height:31px;color:var(--white);font-size:15px}
.socials{left:113px;top:3266px;display:flex;gap:5px}
.socials span{width:32px;height:32px;border:1.5px solid var(--white);border-radius:50%;display:flex;align-items:center;justify-content:center}
.socials span i{width:8px;height:8px;background:var(--white);border-radius:50%}
.vline{position:absolute;top:3084px;height:237px;border-left:1px dashed #888}
.detail-icon{position:absolute;left:355px;width:34px;height:34px;border:1.5px solid var(--white);border-radius:50%;display:flex;align-items:center;justify-content:center}
.detail-label{position:absolute;left:400px;color:var(--white);font-size:18px}
.detail-value{position:absolute;left:400px;color:var(--white);font-size:16px;line-height:26px;white-space:nowrap}
.dotline{position:absolute;left:355px;width:240px;border-top:1px dashed #888}
.input{position:absolute;left:731px;width:353px;height:38px;border:1px solid #ddd;color:var(--white);font-size:14px;padding:0 12px;display:flex;align-items:center}
.submit{left:731px;top:3256px;width:353px;height:37px;font-family:'Lato',sans-serif;font-weight:700;font-size:17px;border-radius:2px;box-shadow:none}
.rule{left:99px;top:3382px;width:1002px;border-top:1px solid #666}
.copy{left:0;width:1200px;top:3400px;text-align:center;color:var(--white);font-size:15px}
</style>
</head>
<body>

<!-- header -->
<div class="abs brand">DPM</div>
<div class="abs brand-sub">DELVANE PITCHING MECHANICS</div>
<nav class="nav">
  <a class="active" style="left:477px">Home</a>
  <a style="left:566px">About Us</a>
  <a style="left:686px">Services</a>
  <a style="left:801px">Our Gallery</a>
</nav>
<div class="btn nav-cta">Contact Us</div>

<!-- hero -->
<div class="abs hero" role="img" aria-label="Stadium scene with a pitcher gripping a baseball in the foreground"></div>
<div class="abs display hero-welcome">Welcome To</div>
<h1 class="abs display hero-title">Delvane Pitching<br>Mechanics</h1>
<p class="abs hero-text">Lorem ipsum dolor sit amet, consectetur adipiscing elit, sed do eiusmod tempor incididunt ut labore et dolore magna aliqua.</p>
<div class="btn hero-btn">Get Started</div>
<div class="abs contact-card">
  <h2>Contact Information</h2>
  <p>Contrary to popular belief</p>
  <div class="field"></div>
  <div class="btn">Request Sessions</div>
</div>
<div class="abs dots"><span></span><span class="on"></span><span></span></div>

<!-- about -->
<div class="abs eyebrow about-eyebrow"><em>About</em> Us</div>
<h2 class="abs display about-title">Delvane Pitching<br>Mechanics</h2>
<p class="abs about-lead">Lorem ipsum dolor sit amet, consectetur adipiscing elit, sed do eiusmod tempor incididunt ut labore et dolore magna aliqua. Ut enim ad minim veniam, quis nostrud exercitation ullamco laboris nisi ut aliquip ex ea commodo consequat.</p>
<p class="abs about-body">Sed ut perspiciatis unde omnis iste natus error sit voluptatem accusantium doloremque laudantium, totam rem aperiam, eaque ipsa quae ab illo inventore veritatis et quasi architecto beatae vitae dicta sunt explicabo. Nemo enim ipsam voluptatem quia voluptas sit aspernatur aut odit aut fugit, sed quia consequuntur magni dolores eos qui ratione voluptatem sequi nesciunt. consectetur, adipisci velit, sed quia non numquam eius modi tempora incidunt ut labore et dolore magnam aliquam quaerat voluptatem.</p>
<div class="abs about-frame"></div>
<div class="photo photo-pitch" role="img" aria-label="Pitcher mid-throw on a dusty stadium mound"></div>
<div class="photo photo-dive" role="img" aria-label="Fielder diving for a ball with glove outstretched"></div>

<!-- services -->
<div class="abs services"></div>
<h2 class="section-title" style="top:1555px">Our <em>Services</em></h2>
<svg class="circle-arrow" style="left:58px;top:1786px" viewBox="0 0 28 28"><circle cx="14" cy="14" r="13" fill="none" stroke="#888" stroke-width="1.5"/><path d="M16 9l-5 5 5 5" fill="none" stroke="#888" stroke-width="1.5"/></svg>
<svg class="circle-arrow" style="left:1114px;top:1786px" viewBox="0 0 28 28"><circle cx="14" cy="14" r="13" fill="none" stroke="#111" stroke-width="1.5"/><path d="M12 9l5 5-5 5" fill="none" stroke="#111" stroke-width="1.5"/></svg>
<div class="card" style="left:111px">
  <div class="photo" role="img" aria-label="Softball pitcher releasing a pitch" style="background:linear-gradient(160deg,#5a6f8a,#b8c4d6 50%,#8a6c4e)"></div>
  <h3>Baseball Pitcher</h3><a>Read More</a>
</div>
<div class="card featured" style="left:441px">
  <div class="photo" role="img" aria-label="Player holding a baseball in an open field" style="background:linear-gradient(160deg,#a8b98a,#3f6fb0 55%,#d9b77a)"></div>
  <h3>Baseball Pitcher</h3><a>Read More</a>
</div>
<div class="card" style="left:770px">
  <div class="photo" role="img" aria-label="Pitcher in red with a large baseball on dark backdrop" style="background:linear-gradient(120deg,#2a2222,#111 50%,#d8d8d8)"></div>
  <h3>Baseball Pitcher</h3><a>Read More</a>
</div>

<!-- division band -->
<div class="abs band"></div>
<h2 class="band-title">Division 1 WJAL baseball pitcher</h2>
<p class="abs band-text">Lorem ipsum dolor sit amet, consectetur adipiscing elit, sed do eiusmod tempor incididunt ut labore et dolore magna aliqua. Ut enim ad minim veniam, quis nostrud exercitation ullamco laboris nisi ut aliquip ex ea commodo consequat. Duis aute irure dolor in reprehenderit in voluptate velit esse cillum dolore eu fugiat nulla pariatur. Excepteur sint occaecat cupidatat non proident, sunt in culpa qui officia deserunt mollit anim id est laborum.Sed ut perspiciatis unde omnis iste natus error sit voluptatem accusantium doloremque laudantium, totam rem aperiam, eaque ipsa quae ab illo inventore veritatis et quasi architecto beatae vitae dicta sunt explicabo.</p>
<div class="abs band-btn">View More</div>

<!-- gallery -->
<h2 class="section-title" style="top:2525px">Our <em>Gallery</em></h2>
<svg class="chev" style="left:66px" viewBox="0 0 14 18"><path d="M9 4l-5 5 5 5" fill="none" stroke="#666" stroke-width="1.5"/></svg>
<svg class="chev" style="left:1122px" viewBox="0 0 14 18"><path d="M5 4l5 5-5 5" fill="none" stroke="#111" stroke-width="2"/></svg>
<div class="gallery">
  <div class="photo" role="img" aria-label="Baseball in flight over a blurred green field" style="left:111px;background:linear-gradient(160deg,#3d4a3a,#1f2a22 60%,#556048)"></div>
  <div class="photo" role="img" aria-label="Softball pitcher on a clay field" style="left:358px;background:linear-gradient(180deg,#2c3322,#5a4a36 40%,#b57e55)"></div>
  <div class="photo" role="img" aria-label="Pitcher in red jersey winding up on the mound" style="left:606px;background:linear-gradient(180deg,#7c8a3e,#4e5a2c 45%,#9c6a4a)"></div>
  <div class="photo" role="img" aria-label="Pitcher in dark uniform against a misty backdrop" style="left:853px;background:linear-gradient(160deg,#c8d2dc,#7f8a96 50%,#3a4450)"></div>
</div>

<!-- footer -->
<div class="abs footer"></div>
<h4 class="footer-heading" style="left:113px">Quick Links</h4>
<ul class="abs quick">
  <li><svg width="13" height="12" viewBox="0 0 13 12"><path d="M1 6h9M6 1l5 5-5 5" fill="none" stroke="#fff" stroke-width="2"/></svg>Home</li>
  <li><svg width="13" height="12" viewBox="0 0 13 12"><path d="M1 6h9M6 1l5 5-5 5" fill="none" stroke="#fff" stroke-width="2"/></svg>About Us</li>
  <li><svg width="13" height="12" viewBox="0 0 13 12"><path d="M1 6h9M6 1l5 5-5 5" fill="none" stroke="#fff" stroke-width="2"/></svg>Services</li>
  <li><svg width="13" height="12" viewBox="0 0 13 12"><path d="M1 6h9M6 1l5 5-5 5" fill="none" stroke="#fff" stroke-width="2"/></svg>Our Gallery</li>
  <li><svg width="13" height="12" viewBox="0 0 13 12"><path d="M1 6h9M6 1l5 5-5 5" fill="none" stroke="#fff" stroke-width="2"/></svg>Contact Us</li>
</ul>
<div class="abs socials"><span><i></i></span><span><i></i></span><span><i></i></span><span><i></i></span></div>
<div class="vline" style="left:318px"></div>

<h4 class="footer-heading" style="left:355px">Contact Details</h4>
<div class="detail-icon" style="top:3111px"><svg width="14" height="14" viewBox="0 0 14 14"><path d="M3 1l2 3-1.5 1.5a8 8 0 0 0 5 5L10 9l3 2-1 2C6 13 1 8 1 2z" fill="#fff"/></svg></div>
<div class="detail-label" style="top:3097px">Phone;</div>
<div class="detail-value" style="top:3127px">+1 555 014 2290</div>
<div class="dotline" style="top:3164px"></div>
<div class="detail-icon" style="top:3174px"><svg width="14" height="11" viewBox="0 0 14 11"><rect x="0" y="0" width="14" height="11" rx="1" fill="#fff"/><path d="M1 1l6 5 6-5" fill="none" stroke="#000" stroke-width="1.3"/></svg></div>
<div class="detail-label" style="top:3179px">Email:</div>
<div class="detail-value" style="top:3208px">info@delvanepitching.example</div>
<div class="dotline" style="top:3245px"></div>
<div class="detail-icon" style="top:3266px"><svg width="12" height="16" viewBox="0 0 12 16"><path d="M6 0a6 6 0 0 1 6 6c0 4-6 10-6 10S0 10 0 6a6 6 0 0 1 6-6z" fill="#fff"/><circle cx="6" cy="6" r="2" fill="#000"/></svg></div>
<div class="detail-label" style="top:3271px">Address:</div>
<div class="detail-value" style="top:3296px">Delvane Pitching Mechanics<br>United State.</div>
<div class="vline" style="left:686px"></div>

<h4 class="footer-heading" style="left:731px">Contact Me</h4>
<div class="input" style="top:3097px">Name:</div>
<div class="input" style="top:3150px">Email:</div>
<div class="input" style="top:3203px">Address:</div>
<div class="btn submit">Submit Now</div>
<div class="abs rule"></div>
<div class="abs copy">Copyrights@2023.Delvane Pitching Mechanics.All Rights Reserved</div>

</body>
</html>
```